Stonebrook Business Card Redesign & Logo Update

We need to update our business cards to something more modern and fresh. Stonebrook can provide the current color schemes and old design examples, but welcome creativity in helping us with this redesign. PLEASE NOTE that we no longer utilize the "tree" and/or "leaf" imagery in our branding. If able would apprecaite an update on the quality of our "words only" logo in Ai. / PNG formats too.

Target Market(s)

Investors, landowners, corporate partners, contractors

Industry/Entity Type

Environmental Restoration & Conservation

Contact Information for Business Card

Logo, persons name, title, mailing address, phone and email, website url

Font styles to use
Other font styles liked:
• Merriweather

Requirements
Nice to have
• Logo, persons name, title, mailing address, phone and email, website url, but open to ideams
Should not have
• No all back backgrounds

```html
<!DOCTYPE html>
<html lang="en">
<head>
<meta charset="utf-8">
<title>Stonebrook Business Card</title>
<link href="https://fonts.googleapis.com/css2?family=Oswald:wght@500;600&family=Roboto:wght@400&display=swap" rel="stylesheet">
<style>
  :root {
    --backdrop: #e4e4e4;
    --card-white: #f6f6f6;
    --brand-orange: #e07b0c;
    --brand-green: #1e8a3c;
    --brand-green-light: #2fa35c;
    --card-green: #1c8236;
    --card-green-dark: #146a2a;
    --ink: #1a1a1a;
    --ink-soft: #5c5c5c;
    --rule: #b8b8b8;
  }
  html, body {
    margin: 0;
    padding: 0;
    width: 1200px;
    height: 1200px;
    overflow: hidden;
    background: var(--backdrop);
  }
  .card {
    position: absolute;
    left: 262px;
    width: 686px;
    height: 392px;
    border-radius: 20px;
    overflow: hidden;
  }
  .card-front { top: 165px; background: var(--card-white); }
  .card-back  { top: 653px; background: var(--card-green); }

  .wordmark {
    position: absolute;
    left: 80px;
    top: 152px;
    width: 276px;
    text-align: center;
    white-space: nowrap;
  }
  .wordmark-name {
    display: block;
    font-family: "Oswald", sans-serif;
    font-weight: 600;
    font-size: 54px;
    line-height: 60px;
    letter-spacing: -1.5px;
    color: var(--brand-green-light);
  }
  .wordmark-tagline {
    display: block;
    font-family: "Oswald", sans-serif;
    font-weight: 500;
    font-size: 18.5px;
    line-height: 22px;
    letter-spacing: -0.3px;
    color: var(--ink);
    margin-top: 2px;
  }

  .divider {
    position: absolute;
    left: 370px;
    top: 104px;
    width: 1px;
    height: 204px;
    background: var(--rule);
  }

  .contact {
    position: absolute;
    left: 393px;
    top: 100px;
    font-family: "Roboto", sans-serif;
    color: var(--ink-soft);
    white-space: nowrap;
  }
  .person-name {
    font-family: "Oswald", sans-serif;
    font-weight: 500;
    font-size: 26px;
    line-height: 32px;
    margin: 0;
  }
  .person-first { color: var(--brand-orange); }
  .person-last  { color: var(--brand-green); }
  .person-title { font-size: 15px; line-height: 18px; margin: 0 0 9px; }
  .address { font-size: 16px; line-height: 21px; margin: 0 0 7px; font-style: normal; }
  .contact-list { list-style: none; margin: 0; padding: 0; }
  .contact-list li {
    display: flex;
    align-items: center;
    font-size: 16px;
    line-height: 20.5px;
  }
  .contact-list svg { width: 14px; height: 14px; margin-right: 11px; flex: none; }

  .back-field {
    position: absolute;
    inset: 0;
    background: linear-gradient(90deg, var(--card-green-dark) 0%, var(--card-green) 60%, var(--brand-green-light) 100%);
  }
  .back-wordmark {
    left: 348px;
    top: 268px;
    width: 160px;
    color: #ffffff;
  }
  .back-wordmark .wordmark-name { font-size: 33px; line-height: 38px; color: #ffffff; letter-spacing: -1px; }
  .back-wordmark .wordmark-tagline { font-size: 11px; line-height: 13px; color: #ffffff; margin-top: 0; letter-spacing: -0.2px; }
</style>
</head>
<body>
  <section class="card card-front">
    <div class="wordmark">
      <span class="wordmark-name">STONEBROOK</span>
      <span class="wordmark-tagline">ENVIRONMENTAL CREDIT COMPANY</span>
    </div>
    <div class="divider"></div>
    <div class="contact">
      <p class="person-name"><span class="person-first">DANIEL</span> <span class="person-last">MARSH</span></p>
      <p class="person-title">Managing Director</p>
      <address class="address">2140 Alder Ridge Road<br>Juneau, Alaska 99801</address>
      <ul class="contact-list">
        <li>
          <svg viewBox="0 0 16 16"><path fill="#e07b0c" d="M3.5 1.5l2.5 3-1.5 1.8c.9 1.9 2.3 3.3 4.2 4.2L10.5 9l3 2.5-1.2 2.5C7 13.6 2.4 9 2 3.7z"/></svg>
          555-214-7730
        </li>
        <li>
          <svg viewBox="0 0 16 16"><rect x="4" y="1" width="8" height="14" rx="1.5" fill="#e07b0c"/><rect x="5.5" y="3" width="5" height="9" fill="#f6f6f6"/></svg>
          555-381-6042
        </li>
        <li>
          <svg viewBox="0 0 16 16"><rect x="1" y="3.5" width="14" height="9" fill="#e07b0c"/><path d="M1.5 4l6.5 5 6.5-5" fill="none" stroke="#f6f6f6" stroke-width="1.2"/></svg>
          info@stonebrook.com
        </li>
        <li>
          <svg viewBox="0 0 16 16"><circle cx="8" cy="8" r="7" fill="#e07b0c"/><circle cx="6" cy="6.5" r="2.2" fill="#f6f6f6"/><circle cx="10.5" cy="11" r="1.5" fill="#f6f6f6"/></svg>
          www.stonebrook.com
        </li>
      </ul>
    </div>
  </section>

  <section class="card card-back">
    <div class="back-field" role="img" aria-label="Repeating embossed pattern of the company name across the green card back"></div>
    <div class="wordmark back-wordmark">
      <span class="wordmark-name">STONEBROOK</span>
      <span class="wordmark-tagline">ENVIRONMENTAL CREDIT COMPANY</span>
    </div>
  </section>
</body>
</html>
```